Up to the Challenge? Canadian based consulting company needs a two sided business card design

A Canadian based security risk management consulting company needs a two-sided business card design. What we do is provide advice and guidance related to emergency, security and business continuity management for small, medium and large companies to help ensure the protection of their people, assets, information, services, operations and reputation.

The final design should be simple, only one or two colours, eye catching, professional and one that makes people look at three or more times just because it looks so darn good.

I have include examples of business cards I like.

Target Market(s)

Small, medium and large companies.

Industry/Entity Type

Security

Contact Information for Business Card

Business Card Size: Standard size of 3.5" (89mm) x 2.0" (51mm) - (see full specifications and guides on PRINTLY's website if required)
Card Stock: Looking to use PRINTLY's Velm 32pt stock textured paper - seam colour either chili red or black
Business Name: The Harrowgate Partners
Website: www.theharrowgatepartners.example
Telephone: (555)310-2968
Name: Dana Ostrander
Position: Principle
e-mail: Dana.Ostrander@theharrowgatepartners.example

Font styles to use
Serif

Colors
ec1f27
000000
9d9d9d
aaaaaa
606060

Requirements
Must have
• - "The Harrowgate Partners" logo (see uploaded files). I have included grey scale and colour versions.
• - Business card details (as above)
Nice to have
• - One side black or grey scale.
• - Other side would likely be white.
• - Everyone likes the silver logo on the black background.
• - Small element of colour i.e. red but I'm leaning more to greyscale.
Should not have
• - A lot of colour. Keep it simple.

```html
<!DOCTYPE html>
<html lang="en">
<head>
<meta charset="utf-8">
<title>The Harrowgate Partners — Business Card</title>
<link rel="stylesheet" href="https://fonts.googleapis.com/css2?family=Cinzel:wght@500&family=Merriweather:wght@700&family=Montserrat:wght@400&display=swap">
<style>
  :root {
    --page-bg: #e6e6e6;
    --card-dark: #3d3d3d;
    --card-dark-edge: #2e2e2e;
    --card-light: #ffffff;
    --ink-dark: #3a3a3a;
    --ink-mid: #606060;
    --ink-soft: #9d9d9d;
    --silver: #f2f2f2;
    --decor-dark: #555555;
    --decor-light: #eeeeee;
  }
  * { box-sizing: border-box; margin: 0; padding: 0; }
  html, body { width: 1200px; height: 1000px; overflow: hidden; }
  body { background: var(--page-bg); position: relative; }
  .card {
    position: absolute;
    left: 250px;
    width: 700px;
    height: 400px;
    border-radius: 22px;
    overflow: hidden;
    box-shadow: 0 10px 30px rgba(0,0,0,0.18);
  }
  /* Front side */
  .card--front {
    top: 70px;
    background: linear-gradient(135deg, var(--card-dark) 0%, var(--card-dark-edge) 100%);
  }
  .card--front .decor {
    position: absolute;
    right: -40px;
    top: -30px;
    width: 380px;
    height: 330px;
    border-radius: 50%;
    background: radial-gradient(ellipse at center, var(--decor-dark) 0%, rgba(85,85,85,0) 70%);
    opacity: 0.8;
  }
  .brand {
    display: flex;
    align-items: center;
    font-family: 'Cinzel', serif;
    font-weight: 500;
  }
  .brand__mark { background: currentColor; flex: none; }
  .card--front .brand {
    position: absolute;
    left: 120px;
    top: 140px;
    gap: 22px;
    color: var(--silver);
    font-size: 36px;
    line-height: 1.15;
    letter-spacing: 1px;
  }
  .card--front .brand__mark { width: 70px; height: 70px; }
  .brand__name { text-align: center; }
  .brand__name span { display: block; }
  .brand__name span + span { font-size: 24px; letter-spacing: 4px; }
  /* Back side */
  .card--back {
    top: 530px;
    background: var(--card-light);
  }
  .card--back .decor {
    position: absolute;
    right: -20px;
    top: -20px;
    width: 420px;
    height: 420px;
    border-radius: 50%;
    background: radial-gradient(ellipse at center, var(--decor-light) 0%, rgba(238,238,238,0) 70%);
  }
  .card--back .edge-tab {
    position: absolute;
    left: 0;
    top: 230px;
    width: 14px;
    height: 170px;
    background: var(--ink-dark);
    border-radius: 0 8px 0 0;
  }
  .back-header {
    position: absolute;
    left: 46px;
    right: 46px;
    top: 46px;
    display: flex;
    align-items: center;
    gap: 20px;
  }
  .card--back .brand {
    color: var(--ink-mid);
    font-size: 18px;
    gap: 12px;
    white-space: nowrap;
  }
  .card--back .brand__mark { width: 36px; height: 36px; }
  .rule { flex: 1; height: 1px; background: var(--ink-soft); }
  .person {
    position: absolute;
    left: 60px;
    top: 200px;
  }
  .person__name {
    font-family: 'Merriweather', serif;
    font-weight: 700;
    font-size: 28px;
    color: var(--ink-dark);
  }
  .person__role {
    display: flex;
    align-items: center;
    gap: 10px;
    margin-top: 4px;
    font-family: 'Montserrat', sans-serif;
    font-size: 15px;
    color: var(--ink-mid);
  }
  .person__role::after {
    content: "";
    width: 140px;
    height: 1px;
    background: var(--ink-soft);
  }
  .contacts {
    list-style: none;
    margin-top: 16px;
    font-family: 'Montserrat', sans-serif;
    font-size: 15px;
    color: var(--ink-mid);
  }
  .contacts li {
    display: flex;
    align-items: center;
    gap: 10px;
    line-height: 26px;
  }
  .contacts svg { width: 12px; height: 12px; fill: var(--ink-mid); flex: none; }
</style>
</head>
<body>
  <section class="card card--front" aria-label="Card front">
    <div class="decor" role="img" aria-label="Faint leafy branch decoration"></div>
    <div class="brand">
      <span class="brand__mark"></span>
      <span class="brand__name"><span>The Harrowgate</span><span>Partners</span></span>
    </div>
  </section>

  <section class="card card--back" aria-label="Card back">
    <div class="decor" role="img" aria-label="Faint leafy branch decoration"></div>
    <div class="edge-tab"></div>
    <div class="back-header">
      <div class="brand"><span class="brand__mark"></span><span>The Harrowgate Partners</span></div>
      <div class="rule"></div>
    </div>
    <div class="person">
      <h1 class="person__name">Dana Ostrander</h1>
      <p class="person__role">Principle</p>
      <ul class="contacts">
        <li><svg viewBox="0 0 12 12"><path d="M2.5 0.5 L4.5 0.5 L5 3.2 L3.6 4.3 Q4.8 6.9 7.7 8.4 L8.8 7 L11.5 7.5 L11.5 9.5 Q11.5 11.5 9.5 11.5 Q0.5 10.5 0.5 2.5 Q0.5 0.5 2.5 0.5 Z"/></svg>(555)310-2968</li>
        <li><svg viewBox="0 0 12 12"><path d="M0.5 2 H11.5 V10 H0.5 Z M1.5 3 L6 6.5 L10.5 3 Z" fill-rule="evenodd"/></svg>Dana.Ostrander@theharrowgatepartners.example</li>
        <li><svg viewBox="0 0 12 12"><circle cx="6" cy="6" r="5.5"/></svg>www.theharrowgatepartners.example</li>
      </ul>
    </div>
  </section>
</body>
</html>
```